Business Card Design Project

I need a business card design for our new logo, please check the logo at the following link:
https://www.filecrate.net/s/q7rtx2pw9kd41m/FernLoop.png
The address on the business card:
Av. Gervásio Tavares 418 sala 207
Barra da Tijuca, Rio de Janeiro, RJ
CEP: 22714-380
Brasil
Phone: +55 21 86347215
e-mail: osvaldo@fernloop.com.br
Updates
Thank you all for sending your designs, we will not provide feedback because there are too many designs, on December 3 we will pick the best design according to our point of view. Please keep posting.
Osvaldo
Industry/Entity Type
Business
Look and feel
Each slider illustrates characteristics of the customer's brand and the style your logo design should communicate.

```html
<!DOCTYPE html>
<html lang="pt-BR">
<head>
<meta charset="UTF-8">
<title>FernLoop — Business Card</title>
<link href="https://fonts.googleapis.com/css2?family=Barlow+Semi+Condensed:wght@400;700&display=swap" rel="stylesheet">
<style>
  :root {
    --backdrop: #e8e5df;
    --brand-yellow: #fdc20c;
    --card-white: #ffffff;
    --ink: #1a1a1a;
  }
  html, body {
    margin: 0;
    padding: 0;
    width: 1200px;
    height: 893px;
    overflow: hidden;
    background: var(--backdrop);
  }
  .canvas {
    position: relative;
    width: 1200px;
    height: 893px;
  }
  .business-card {
    position: absolute;
    left: 80px;
    top: 158px;
    width: 1040px;
    height: 577px;
    box-shadow: 0 6px 18px rgba(0,0,0,0.18);
  }
  .business-card svg {
    display: block;
    width: 100%;
    height: 100%;
  }
  .card-base { fill: var(--brand-yellow); }
  .info-panel { fill: var(--card-white); }
  .contact-text {
    font-family: "Barlow Semi Condensed", "Arial Narrow", sans-serif;
    font-weight: 400;
    font-size: 19px;
    fill: var(--ink);
  }
  .brand-name {
    font-family: "Barlow Semi Condensed", "Arial Narrow", sans-serif;
    font-weight: 700;
    font-size: 31px;
    fill: var(--ink);
  }
  .brand-dot { fill: var(--brand-yellow); }
</style>
</head>
<body>
<main class="canvas">
  <section class="business-card" aria-label="FernLoop business card">
    <svg viewBox="0 0 665 369" xmlns="http://www.w3.org/2000/svg">
      <defs>
        <clipPath id="card-edge">
          <rect x="0" y="0" width="665" height="369"/>
        </clipPath>
      </defs>
      <rect class="card-base" x="0" y="0" width="665" height="369"/>
      <g clip-path="url(#card-edge)">
        <path class="info-panel"
              d="M76,48.5 L700,-18 L700,289 L106,350.5
                 Q93,352 91.5,339 L62.5,62 Q61,50 76,48.5 Z"/>
      </g>

      <g class="brand-lockup">
        <circle class="brand-dot" cx="192" cy="168" r="24"/>
        <text class="brand-name" x="138" y="238">FernLoop</text>
      </g>

      <g class="contact-block" transform="rotate(-5.5 312 80)">
        <text class="contact-text" x="312" y="80">Av. Gervásio Tavares 418 sala 207</text>
        <text class="contact-text" x="312" y="103">Barra da Tijuca, Rio de Janeiro, RJ</text>
        <text class="contact-text" x="312" y="126">CEP: 22714-380</text>
        <text class="contact-text" x="314" y="149">Brasil</text>
        <text class="contact-text" x="314" y="252">Phone: +55 21 86347215</text>
        <text class="contact-text" x="314" y="275">e-mail: osvaldo@fernloop.com.br</text>
      </g>
    </svg>
  </section>
</main>
</body>
</html>
```